Redo our website for our Robotics company

We sell robotic equipment to the restaurant industry. Our current robot, is a cooking robot that cooks up to 15 lbs of food. We will provide a prior website as well as brand guidelines. We plan on using wordpress and take advantage of wordpress's visual (no code) editor.

Current website - https://kelvatrix482.com/ (please note we are only selling Pindle now and no longer selling Quado+

We want someone to take our existing content and design the website as well as layout our content we provide. Here's a suggested site layout:

✅ KelvaTrix482 Website Wireframe / Site Map
1. Home

Purpose: Introduce Pindle, establish credibility, drive demo requests.

Sections:

Hero Section

Headline: “Meet Pindle — Your New Robotic Chef for High-Volume, Consistent Cooking.”

Sub-headline: Increase throughput. Reduce labor. Deliver perfect food every time.

CTA: Request a Demo + Watch Pindle Cook

Visual: Video loop or hero animation of Pindle in action.

How Pindle Works (3-4 steps)

Step cards: Load Ingredients → Select Recipe → Pindle Cooks → Serve

Icons and short explanations.

Key Benefits

Labor savings

Zero inconsistency

24/7 uptime

Throughput increases (30–50% faster)

Health & safety compliance

Who It’s For

QSR restaurants

Fast casual

Catering/commissaries

Ghost kitchens

Case Studies / Testimonials

Logo bar + quotes

“Pindle helped us reduce cooking times by 40%.”

Video Section

“Watch Pindle cook a full batch from start to finish.”

CTA Section

Big banner: Book a Demo

2. Product: “Meet Pindle”

Purpose: Deep dive into hardware, software, safety, reliability.

Sections:

Overview

What Pindle is

What tasks it automates

Where it fits in a kitchen

Hardware Features

High-temperature cooking chamber

Precision sensors

Automated stirring

Automated dispensing

Safety mechanisms (locking lids, auto-shutoff)

Software & AI

Recipe automation

IoT dashboard

Remote monitoring

Predictive maintenance

Specs Table

Dimensions

Power requirements

Capacity (lbs per batch)

Safety certifications

Gallery

Close-ups, installation photos, process shots

CTA: Request a Demo

3. Solutions

Purpose: Show that Pindle solves real operational problems.

Sub-pages or sections:

For Quick-Service Restaurants

Reduce labor cost

Speed up peak-hour demand

For Catering & Commissaries

Large-batch consistency

Automate repetitive cooking tasks

For High-Growth Chains

Replicable quality across multiple locations

Centralized recipe control

Each solution page includes:

A problem statement

How Pindle solves it

Metrics / KPIs

Relevant testimonial

CTA

4. ROI / Economics

Purpose: Sell the financial story clearly.

Sections:

Savings Calculator

Labor hours saved

Cost savings

Throughput increases

Food waste reduction

Before & After Comparison

Traditional kitchen vs. robotic kitchen

Sample ROI

“Payback in as little as 3–6 months.”

Download Full ROI Report (PDF)

5. Case Studies

Purpose: Social proof + real results.

Structure for each case study:

Customer background

Problem

Implementation

KPIs achieved

Labor savings

Consistency improvements

Cooking speed

Quote + photos/video

6. Pricing

Purpose: Start a commercial conversation.

Include:

Subscription model (monthly / annual)

Hardware leasing or purchase options

Installation + training

Support level

CTA to book a sales call

7. About

Purpose: Build trust.

Sections:

Mission statement

Founding team

Advisors/partners

“Why we built Pindle”

8. Resources

Purpose: SEO + education.

Subpages:

Blog (e.g., “The Future of Automated Kitchens”)

Whitepapers

Technical documentation

Product videos

9. Contact

General inquiry form

Sales contact

Support portal

Careers

```html
<!DOCTYPE html>
<html lang="en">
<head>
<meta charset="utf-8">
<title>KelvaTrix482 — Meet Pindle</title>
<link href="https://fonts.googleapis.com/css2?family=Poppins:wght@400;500;600;700;800;900&display=swap" rel="stylesheet">
<style>
:root{
  --orange:#f5874b;
  --red:#ee4d3a;
  --brand:#ef4a38;
  --ink:#111111;
  --text:#3a3a3a;
  --pink:#fde9e5;
  --pink-2:#fbdcd6;
  --white:#ffffff;
  --black:#050505;
  --line:#ececec;
}
*{box-sizing:border-box;margin:0;padding:0}
html,body{width:1200px;height:3029px;overflow:hidden}
body{position:relative;background:var(--white);font-family:"Poppins",sans-serif;color:var(--ink)}
.abs{position:absolute}
.bg-shapes{position:absolute;left:0;top:0;width:1200px;height:3029px}

/* header */
.logo{position:absolute;font-family:"Poppins",sans-serif;font-weight:800;color:var(--brand);letter-spacing:-.5px}
.header-logo{left:147px;top:22px;font-size:25px}
.nav-item{position:absolute;top:30px;font-size:9px;font-weight:600;color:var(--ink);white-space:nowrap}
.nav-home{position:absolute;left:503px;top:30px;width:11px;height:11px}
.btn{position:absolute;display:flex;align-items:center;justify-content:center;font-size:9.5px;font-weight:600;transform:skewX(-14deg);border-radius:6px;white-space:nowrap}
.btn span{transform:skewX(14deg)}
.btn-head{left:942px;top:20px;width:106px;height:31px;background:var(--red);color:var(--white);font-size:9px}

/* hero */
.hero-title{left:146px;top:172px;width:470px;font-size:41px;line-height:41px;font-weight:900;color:var(--white);letter-spacing:-.3px}
.hero-sub{left:146px;top:355px;font-size:10.5px;color:var(--white)}
.btn-hero-1{left:150px;top:385px;width:108px;height:30px;background:var(--white);color:var(--red);font-size:9px}
.btn-hero-2{left:268px;top:385px;width:116px;height:30px;border:1.5px solid var(--white);color:var(--white);font-size:9px}
.hero-visual{left:608px;top:141px;width:592px;height:383px;border-radius:18px;background:linear-gradient(160deg,#5e6266 0%,#b9bcbf 45%,#8b8f93 100%)}

/* steps */
.section-title{position:absolute;left:0;width:1200px;text-align:center;font-weight:800;color:var(--ink)}
.works-title{top:638px;font-size:26px}
.card{position:absolute;transform:skewX(-8deg);border-radius:18px;border:1px solid var(--line);background:var(--white)}
.card .inner{transform:skewX(8deg)}
.step-card{top:691px;width:212px;height:241px}
.step-card .inner{position:absolute;left:28px;top:52px;width:160px}
.step-card .icon{width:36px;height:36px;margin-bottom:10px}
.step-num{font-size:11.5px;font-weight:700}
.step-name{font-size:12.5px;font-weight:700;margin-top:7px}
.step-text{font-size:10.3px;line-height:15.5px;color:var(--text);margin-top:8px}
.step-card.active{background:linear-gradient(160deg,var(--orange),var(--red));border:none}
.step-card.active .step-num,.step-card.active .step-name,.step-card.active .step-text{color:var(--white)}

/* benefits */
.benefit-panel{left:191px;top:1018px;width:299px;height:458px;background:var(--pink);border:none}
.machine-visual{left:247px;top:1021px;width:212px;height:455px;border-radius:6px;background:linear-gradient(180deg,#9fa3a7 0%,#6f7377 30%,#c9cccf 60%,#8d9195 100%)}
.benefits-title{left:628px;top:1058px;font-size:29px;font-weight:800}
.benefit{position:absolute;left:571px;width:470px}
.benefit .b-icon{position:absolute;left:0;top:4px;width:44px;height:44px}
.benefit h3{position:absolute;left:58px;top:0;font-size:13px;font-weight:700}
.benefit p{position:absolute;left:58px;top:22px;width:370px;font-size:10.3px;line-height:15.5px;color:var(--text)}
.divider{position:absolute;left:576px;width:455px;height:1px;background:var(--line)}
.divider::before,.divider::after{content:"";position:absolute;top:-2px;width:5px;height:5px;border-radius:50%;background:var(--red)}
.divider::before{left:-2px}.divider::after{right:-2px}

/* audiences */
.who-title{left:335px;top:1636px;font-size:25px;font-weight:800}
.who-card{top:1682px;width:232px;height:316px;border:none;overflow:hidden}
.who-card .photo{position:absolute;left:6px;top:6px;width:258px;height:154px;border-radius:14px;transform:skewX(8deg);margin-left:-22px}
.who-card .inner{position:absolute;left:14px;top:180px;width:196px}
.who-card h3{font-size:12.5px;font-weight:700;line-height:15px;min-height:18px}
.who-card p{font-size:10.3px;line-height:15.5px;color:var(--text);margin-top:10px}

/* testimonials */
.testi-title{top:2138px;font-size:26px}
.quote{position:absolute;left:0;top:2194px;width:1200px;text-align:center;font-size:19px;line-height:25px;color:var(--ink)}
.dots{position:absolute;left:577px;top:2253px;display:flex;gap:6px}
.dots i{width:7px;height:7px;border-radius:50%;background:#dcdcdc;display:block}
.dots i.on{background:var(--red)}
.partner{position:absolute;top:2294px;width:94px;height:94px;border-radius:50%;background:var(--white);box-shadow:0 10px 18px rgba(238,77,58,.12);display:flex;align-items:center;justify-content:center;font-size:11.5px;font-weight:600;color:#333;text-align:center}

/* cta */
.cta-title{left:266px;top:2545px;font-size:27px;font-weight:800;color:var(--white)}
.cta-text{left:266px;top:2590px;font-size:10.3px;line-height:15.5px;color:var(--white)}
.btn-cta{left:779px;top:2562px;width:110px;height:30px;background:var(--white);color:var(--red);font-size:9px}

/* footer */
.footer-logo{left:147px;top:2770px;font-size:33px}
.footer-tag{left:147px;top:2822px;font-size:17px;font-weight:800;color:var(--white)}
.f-col{position:absolute;top:2732px;color:var(--white)}
.f-col h4{font-size:16px;font-weight:800;margin-bottom:10px;white-space:nowrap}
.f-col li{list-style:none;font-size:10.3px;line-height:15.6px;display:flex;align-items:center;gap:5px;white-space:nowrap}
.f-col.social li{line-height:25px}
.f-col svg{width:9px;height:9px}
.newsletter{position:absolute;left:834px;top:2767px;width:170px;height:30px;background:var(--white);transform:skewX(-14deg);border-radius:6px}
.newsletter span{position:absolute;left:14px;top:8px;transform:skewX(14deg);font-size:10.3px;color:#444}
.newsletter svg{position:absolute;right:14px;top:10px;width:10px;height:10px;transform:skewX(14deg)}

/* bottom bar */
.copyright{left:148px;top:2993px;font-size:10.3px;color:var(--ink)}
.legal{left:883px;top:2993px;font-size:10.3px;font-weight:500;color:var(--ink)}
.to-top{left:1107px;top:2986px;width:28px;height:28px;border-radius:50%;background:var(--red);display:flex;align-items:center;justify-content:center}
</style>
</head>
<body>

<svg class="bg-shapes" viewBox="0 0 1200 3029" aria-hidden="true">
  <defs>
    <linearGradient id="heroGrad" x1="0" y1="0" x2="0.3" y2="1">
      <stop offset="0" stop-color="#f5874b"/>
      <stop offset="1" stop-color="#ee4d3a"/>
    </linearGradient>
    <linearGradient id="ctaGrad" x1="0" y1="0" x2="0.2" y2="1">
      <stop offset="0" stop-color="#f5874b"/>
      <stop offset="1" stop-color="#ee4d3a"/>
    </linearGradient>
  </defs>
  <path d="M0 67 H1118 Q1140 67 1133 88 L1003 530 Q995 551 972 551 H0 Z" fill="url(#heroGrad)"/>
  <path d="M312 1574 H1200 V2059 H164 Q140 2059 147 2037 L288 1594 Q295 1574 312 1574 Z" fill="#fbdcd6"/>
  <path d="M0 2586 H1114 Q1138 2586 1130 2608 L998 2950 Q990 2971 968 2971 H0 Z" fill="#050505"/>
  <path d="M248 2482 H1036 Q1058 2482 1048 2502 L972 2655 Q963 2673 942 2673 H168 Q144 2673 154 2652 L226 2500 Q234 2482 248 2482 Z" fill="url(#ctaGrad)"/>
</svg>

<!-- Header -->
<div class="logo header-logo">KelvaTrix482</div>
<nav>
  <svg class="nav-home" viewBox="0 0 12 12"><path d="M6 1 L11 6 H9.5 V11 H7 V8 H5 V11 H2.5 V6 H1 Z" fill="#ee4d3a"/></svg>
  <span class="nav-item" style="left:533px">Product</span>
  <span class="nav-item" style="left:587px">Solutions</span>
  <span class="nav-item" style="left:646px">Case Studies</span>
  <span class="nav-item" style="left:721px">Pricing</span>
  <span class="nav-item" style="left:771px">About</span>
  <span class="nav-item" style="left:815px">Resources</span>
  <span class="nav-item" style="left:878px">Contact</span>
</nav>
<div class="btn btn-head"><span>Request a Demo</span></div>

<!-- Hero -->
<h1 class="abs hero-title">Meet Pindle Your New Robotic Chef for High Volume, Consistent Cooking.</h1>
<p class="abs hero-sub">Increase throughput. Reduce labor. Deliver perfect food every time.</p>
<div class="btn btn-hero-1"><span>Request a Demo</span></div>
<div class="btn btn-hero-2"><span>Watch Pindle Cook</span></div>
<div class="abs hero-visual" role="img" aria-label="Row of four stainless steel Pindle cooking robots in action"></div>

<!-- How it works -->
<h2 class="section-title works-title">How Pindle Works</h2>

<div class="card step-card" style="left:165px">
  <div class="inner">
    <svg class="icon" viewBox="0 0 36 36"><path d="M4 16 H32 Q31 28 18 30 Q5 28 4 16 Z" fill="#ee4d3a"/><circle cx="12" cy="10" r="4" fill="#f5874b"/><circle cx="21" cy="8" r="4" fill="#ee4d3a"/><rect x="13" y="30" width="10" height="3" rx="1" fill="#ee4d3a"/></svg>
    <div class="step-num">Step 1</div>
    <div class="step-name">Load Ingredients</div>
    <p class="step-text">Simply add your prepped ingredients into Pindle's cooking chamber. No special training required.</p>
  </div>
</div>
<div class="card step-card active" style="left:385px">
  <div class="inner">
    <svg class="icon" viewBox="0 0 36 36"><rect x="7" y="4" width="22" height="26" rx="2" fill="#fff"/><path d="M13 13 Q13 9 18 9 Q23 9 23 13 V17 H13 Z" fill="#ee4d3a"/><rect x="7" y="30" width="22" height="3" fill="#fff"/></svg>
    <div class="step-num">Step 2</div>
    <div class="step-name">Select Recipe</div>
    <p class="step-text">Choose a preset recipe from the touchscreen or upload your own standardized cooking program.</p>
  </div>
</div>
<div class="card step-card" style="left:605px">
  <div class="inner">
    <svg class="icon" viewBox="0 0 36 36"><path d="M12 3 Q10 6 12 9 M18 3 Q16 6 18 9 M24 3 Q22 6 24 9" stroke="#ee4d3a" stroke-width="1.5" fill="none"/><rect x="6" y="13" width="24" height="12" rx="3" fill="#ee4d3a"/><rect x="2" y="15" width="4" height="3" fill="#ee4d3a"/><rect x="30" y="15" width="4" height="3" fill="#ee4d3a"/><path d="M8 28 L6 33 M14 28 L13 33 M22 28 L23 33 M28 28 L30 33" stroke="#ee4d3a" stroke-width="2"/></svg>
    <div class="step-num">Step 3</div>
    <div class="step-name">Pindle Cooks</div>
    <p class="step-text">Pindle handles the entire process automatically — heating, stirring, timing, and monitoring for perfect</p>
  </div>
</div>
<div class="card step-card" style="left:825px">
  <div class="inner">
    <svg class="icon" viewBox="0 0 36 36"><path d="M5 22 Q5 9 18 9 Q31 9 31 22 Z" fill="#ee4d3a"/><circle cx="18" cy="7" r="2.5" fill="#ee4d3a"/><rect x="3" y="23" width="30" height="3" rx="1.5" fill="#ee4d3a"/><path d="M6 29 H26 L30 27" stroke="#ee4d3a" stroke-width="2.5" fill="none"/></svg>
    <div class="step-num">Step4</div>
    <div class="step-name">Serve</div>
    <p class="step-text">Once the batch is ready, Pindle alerts your team. Just open, serve, and keep operations moving.</p>
  </div>
</div>

<!-- Key benefits -->
<div class="card benefit-panel"></div>
<div class="abs machine-visual" role="img" aria-label="Single Pindle cooking robot unit with open chamber and touchscreen"></div>

<h2 class="abs benefits-title">Key Benefits</h2>

<div class="benefit" style="top:1114px">
  <svg class="b-icon" viewBox="0 0 44 44"><path d="M6 10 L16 20 L12 24 L4 16 Z" fill="#ee4d3a"/><path d="M16 20 L30 34" stroke="#ee4d3a" stroke-width="4"/><path d="M22 22 Q30 16 38 22 V32 H24 Z" fill="#f5874b"/></svg>
  <h3>Labor Savings</h3>
  <p>Pindle automates repetitive cooking tasks, reducing dependence on hard-to-find kitchen staff and lowering overall labor costs.</p>
</div>
<div class="divider" style="top:1178px"></div>
<div class="benefit" style="top:1186px">
  <svg class="b-icon" viewBox="0 0 44 44"><rect x="10" y="6" width="22" height="30" rx="2" fill="none" stroke="#ee4d3a" stroke-width="2.5"/><path d="M15 14 H27 M15 20 H27 M15 26 H23" stroke="#f5874b" stroke-width="2"/><path d="M28 30 L38 20" stroke="#ee4d3a" stroke-width="3"/></svg>
  <h3>Zero Inconsistency</h3>
  <p>Every batch is cooked with precise timing, temperature, and stirring — ensuring the same taste and quality across all locations.</p>
</div>
<div class="divider" style="top:1250px"></div>
<div class="benefit" style="top:1258px">
  <svg class="b-icon" viewBox="0 0 44 44"><circle cx="21" cy="23" r="15" fill="none" stroke="#ee4d3a" stroke-width="3"/><path d="M21 14 V23 L27 27" stroke="#f5874b" stroke-width="2.5" fill="none"/><path d="M34 10 L38 16 L31 16 Z" fill="#ee4d3a"/></svg>
  <h3>24/7 Uptime</h3>
  <p>Designed for nonstop food production, Pindle operates reliably throughout the day without breaks, turnover, or downtime.</p>
</div>
<div class="divider" style="top:1322px"></div>
<div class="benefit" style="top:1331px">
  <svg class="b-icon" viewBox="0 0 44 44"><circle cx="16" cy="20" r="9" fill="#ee4d3a"/><circle cx="28" cy="16" r="8" fill="#f5874b"/><path d="M10 34 Q22 26 34 34" stroke="#ee4d3a" stroke-width="3" fill="none"/></svg>
  <h3>30–50% Faster Throughput</h3>
  <p>Pindle increases your kitchen's output by speeding up cooking cycles and maintaining continuous production during peak hours.</p>
</div>
<div class="divider" style="top:1396px"></div>
<div class="benefit" style="top:1403px">
  <svg class="b-icon" viewBox="0 0 44 44"><path d="M10 6 H26 L32 12 V38 H10 Z" fill="#ee4d3a"/><path d="M15 16 H26 M15 22 H26" stroke="#fff" stroke-width="2"/><circle cx="31" cy="32" r="7" fill="#f5874b"/><path d="M28 32 L30.5 34.5 L34 30" stroke="#fff" stroke-width="1.8" fill="none"/></svg>
  <h3>Health &amp; Safety Compliance</h3>
  <p>Built-in safety sensors, closed-cooking chambers, and automated processes reduce contamination risks and improve workplace safety.</p>
</div>

<!-- Who it's for -->
<h2 class="abs who-title">Who It's For</h2>

<div class="card who-card" style="left:308px">
  <div class="photo" role="img" aria-label="Plated dishes being served at a restaurant counter" style="background:linear-gradient(135deg,#2f4b5a,#6d8a94 60%,#c9b9a6)"></div>
  <div class="inner">
    <h3>QSR Restaurants</h3>
    <p>Pindle helps quick-service restaurants keep up with high-volume demand by automating batch cooking and ensuring consistent results during peak hours.</p>
  </div>
</div>
<div class="card who-card" style="left:565px">
  <div class="photo" role="img" aria-label="Fast casual kitchen line preparing bowls of food" style="background:linear-gradient(135deg,#c8232c,#e7d6c9 55%,#f3c54a)"></div>
  <div class="inner">
    <h3>Fast Casual Brands</h3>
    <p>Perfect for operations that need speed and quality. Pindle maintains flavor accuracy across multiple dishes while reducing back-of-house labor pressure.</p>
  </div>
</div>
<div class="card who-card" style="left:823px">
  <div class="photo" role="img" aria-label="Large stainless steel commercial commissary kitchen" style="background:linear-gradient(135deg,#cfd6da,#6f7d86 55%,#2e3940)"></div>
  <div class="inner">
    <h3>Catering &amp;<br>Commissary Kitchens</h3>
    <p>Ideal for large-scale food production. Pindle delivers uniform batches, reduces prep time, and increases output for catering companies and central kitchens.</p>
  </div>
</div>
<div class="card who-card" style="left:1081px">
  <div class="photo" role="img" aria-label="Ghost kitchen staff preparing delivery orders" style="background:linear-gradient(135deg,#3d5a78,#b98a6a 60%,#e6d2c2)"></div>
  <div class="inner">
    <h3>Ghost Kitchens</h3>
    <p>Enables efficient production in compact spaces with limited staff, supports multi-brand menus, and stays reliable, repeatable around the clock.</p>
  </div>
</div>

<!-- Testimonials -->
<h2 class="section-title testi-title">Testimonials</h2>
<p class="quote">Pindle helped us reduce cooking times by 40% and improved<br>consistency across all our locations.</p>
<div class="dots"><i></i><i class="on"></i><i></i><i></i></div>

<div class="partner" style="left:226px">Brightwell</div>
<div class="partner" style="left:335px">Harborline</div>
<div class="partner" style="left:444px">Fizzora</div>
<div class="partner" style="left:552px">Ridgeway</div>
<div class="partner" style="left:660px">Mealcraft</div>
<div class="partner" style="left:769px">Dunmore's</div>
<div class="partner" style="left:878px">Ember Wings</div>

<!-- CTA -->
<h2 class="abs cta-title">Book a Demo Today</h2>
<p class="abs cta-text">Experience firsthand how Pindle can transform your kitchen<br>operations, increase throughput, and ensure perfect food every time.</p>
<div class="btn btn-cta"><span>Request a Demo</span></div>

<!-- Footer -->
<div class="logo footer-logo">KelvaTrix482</div>
<p class="abs footer-tag">Enhance, Not Replace.</p>

<div class="f-col" style="left:422px">
  <h4>Menu</h4>
  <ul><li>Home</li><li>Product</li><li>Solutions</li><li>Case Studies</li><li>Pricing</li><li>About</li><li>Resources</li><li>Contact</li></ul>
</div>
<div class="f-col" style="left:541px">
  <h4>Say Hello</h4>
  <ul>
    <li><svg viewBox="0 0 10 10"><rect x="0.5" y="2" width="9" height="6.5" rx="1" fill="#ee4d3a"/><path d="M1 2.5 L5 5.5 L9 2.5" stroke="#050505" stroke-width="0.8" fill="none"/></svg>info@kelvatrix482.com</li>
    <li style="margin-top:9px"><svg viewBox="0 0 10 10"><path d="M2 1 L4 1 L4.5 3.5 L3.3 4.3 Q4.5 6.5 5.7 6.7 L6.5 5.5 L9 6 L9 8 Q9 9 8 9 Q1 8.5 1 2 Q1 1 2 1 Z" fill="#ee4d3a"/></svg>+1 [555] 014 2873</li>
  </ul>
</div>
<div class="f-col social" style="left:711px">
  <h4 style="margin-bottom:3px">Socials</h4>
  <ul>
    <li><svg viewBox="0 0 10 10"><circle cx="5" cy="5" r="4" fill="#fff"/></svg>Friendbook</li>
    <li><svg viewBox="0 0 10 10"><circle cx="5" cy="5" r="4" fill="#fff"/></svg>Snapgram</li>
    <li><svg viewBox="0 0 10 10"><circle cx="5" cy="5" r="4" fill="#fff"/></svg>Chirper</li>
  </ul>
</div>
<div class="f-col" style="left:831px">
  <h4>Newsletter Signup</h4>
</div>
<div class="newsletter">
  <span>Your email</span>
  <svg viewBox="0 0 10 10"><path d="M1 5 L9 1 L6 9 L5 5.5 Z" fill="#ee4d3a"/></svg>
</div>

<!-- Bottom bar -->
<p class="abs copyright">KelvaTrix482 © 2025. All Rights Reserved.</p>
<p class="abs legal">Privacy Policy &nbsp;|| Terms of Service</p>
<div class="abs to-top"><svg width="10" height="10" viewBox="0 0 10 10"><path d="M2 6.5 L5 3.5 L8 6.5" stroke="#fff" stroke-width="1.5" fill="none"/></svg></div>

</body>
</html>
```